Buch-/E-Book-Cover Autobiographische Kurzgeschichten
Zielgruppe
Ich vermarkte mein Buch selbst. Zielgruppe sind Frauen und Männer, die leichte Lektüre mit Humor und Lebenserfahrung lesen wollen.
Aufgabenstellung
Das Buch hat den Titel 'Sturmflut ohne Ende'.
Der Inhalt sind autobiographische Kurzgeschichten.
Erst verwitwet wagte ich einen Blick über den Zaun. Und tatsächlich war dort das Gras grüner, die Wiese enthielt lebenswichtige Kräuter und bunte Blumen. Da wollte ich hier, nur wie? Ich hatte „Zäune überwinden“ nicht gelernt. Versuch und Irrtum, Feldforschung, Kampf mit mir selbst, ein nie Aufgeben führten mich zum Erfolg, auf die andere Seite. Und die Wiese hält, was sie versprach. Da hatten sich doch der Witwentröster, das Datingportal, der Escort, den ich nicht mit aufs Zimmer nahm, die Aktfotos und und und gelohnt.
Meine autobiographischen Geschichten sind wie ein gutes Parfum mit Kopf-, Herz- und Basisnote. Riech doch einfach mal rein!
Mein Logo ist zu verwenden.
Einige Kurzgeschichten aus dem Buch stehen auf meiner Website, zum Reinlesen bei Bedarf.
Die Katastrophe, der Wendepunkt in meinem Leben, war der Tod meines Mannes.
Meine Website lautet : www.tann-wiese.de

```html
<!DOCTYPE html>
<html lang="de">
<head>
<meta charset="utf-8">
<title>Sturmflut ohne Ende – Buchcover</title>
<link rel="stylesheet" href="https://fonts.googleapis.com/css2?family=Antonio:wght@700&family=Kaushan+Script&family=Open+Sans:wght@400;600&display=swap">
<style>
  :root {
    --page-bg: #e9e6e1;
    --title-red: #a3313d;
    --outline-white: #ffffff;
    --author-ink: #1f1f1f;
    --sky: #c7dae6;
    --sky-haze: #dfe8ec;
    --hill-green: #7f9a55;
    --wheat: #d9ba72;
    --meadow: #8ea35c;
    --gravel: #dccfba;
    --gravel-light: #e6dccb;
    --logo-bg: #ffffff;
    --logo-ink: #9e2a35;
  }
  html, body {
    margin: 0;
    width: 1200px;
    height: 1068px;
    overflow: hidden;
    background: var(--page-bg);
  }
  .cover {
    position: absolute;
    left: 233px;
    top: 0;
    width: 734px;
    height: 1068px;
    overflow: hidden;
  }
  .cover-photo {
    position: absolute;
    inset: 0;
    background: linear-gradient(180deg,
      var(--sky-haze) 0%,
      var(--sky) 22%,
      var(--sky-haze) 31%,
      var(--hill-green) 33%,
      var(--hill-green) 38%,
      var(--wheat) 43%,
      var(--wheat) 52%,
      var(--meadow) 60%,
      var(--meadow) 74%,
      var(--gravel) 80%,
      var(--gravel-light) 100%);
  }
  .author-name {
    position: absolute;
    right: 52px;
    top: 33px;
    margin: 0;
    font-family: "Open Sans", sans-serif;
    font-weight: 400;
    font-size: 24px;
    letter-spacing: 3px;
    color: var(--author-ink);
  }
  .book-title {
    position: absolute;
    left: 0;
    top: 0;
    width: 734px;
    height: 440px;
  }
  .title-word {
    font-family: "Antonio", sans-serif;
    font-weight: 700;
    fill: var(--title-red);
    stroke: var(--outline-white);
    stroke-width: 5px;
    paint-order: stroke;
    stroke-linejoin: round;
  }
  .title-connector {
    font-family: "Kaushan Script", cursive;
    fill: var(--title-red);
    stroke: var(--outline-white);
    stroke-width: 4px;
    paint-order: stroke;
  }
  .publisher-mark {
    position: absolute;
    left: 285px;
    top: 882px;
    width: 198px;
    height: 186px;
    background: var(--logo-bg);
    display: flex;
    align-items: center;
    justify-content: center;
    gap: 8px;
  }
  .publisher-square {
    width: 10px;
    height: 10px;
    background: var(--logo-ink);
  }
  .publisher-name {
    font-family: "Open Sans", sans-serif;
    font-weight: 600;
    font-size: 17px;
    color: var(--logo-ink);
  }
</style>
</head>
<body>
  <main class="cover">
    <div class="cover-photo" role="img" aria-label="Foto: Frau mit Brille in pinkem Kapuzenpulli und heller Hose lehnt am Feldweg, dahinter Mohnblumen, Kornfeld, grüner Hügel und Himmel"></div>

    <p class="author-name">AUTOR NAME</p>

    <svg class="book-title" viewBox="0 0 734 440" role="heading" aria-level="1" aria-label="Sturmflut ohne Ende">
      <text class="title-word" x="686" y="230" text-anchor="end" font-size="178" textLength="490" lengthAdjust="spacingAndGlyphs">STURMFLUT</text>
      <text class="title-word" x="706" y="405" text-anchor="end" font-size="190" textLength="330" lengthAdjust="spacingAndGlyphs">ENDE</text>
      <text class="title-connector" x="265" y="270" font-size="74" transform="rotate(-12 265 270)">ohne</text>
    </svg>

    <div class="publisher-mark">
      <span class="publisher-square"></span>
      <span class="publisher-name">Elo Tann-Wiese</span>
    </div>
  </main>
</body>
</html>
```